Business Card / Appointment Card for Physician

On one side it should give the logo, address, and contact information, and on the other side it should br an Appointment card.

One Side:
Logo (see attached files)
Board Certified American Orthopedic Surgery

1487 Harrowgate Ave.
Suite KM7
Bronx, NY 10527
Tel: (718) 552 - 1948
Fax: (718) 552 - 7210

628 Fourth Ave.
Suite 42
New York, NY 10087
Tel: (212) 734 - 2815

Second Side:
Appointment
give them a choice of Bronx or Mahattan office
For:
Date:
Time:

If you are unable to keep your appointment, please call (718) 263-5102 24hrs in advance.

Target Market(s)

People that need orthopedic surgery

Industry/Entity Type

Business

Contact Information for Business Card

smart and attractive

Requirements
Must have
• logo
• contact information on one side, appointment information on the other

```html
<!DOCTYPE html>
<html lang="en">
<head>
<meta charset="utf-8">
<title>Daniel R. Hollister MD PC – Business &amp; Appointment Card</title>
<link href="https://fonts.googleapis.com/css2?family=Lato:wght@400;700;900&display=swap" rel="stylesheet">
<style>
  :root {
    --bg: #1d1d1f;
    --card: #ffffff;
    --blue: #0f72b5;
    --blue-dark: #0b5e98;
    --green: #7dbd43;
    --ink: #2a2a2a;
    --rule: #4a4a4a;
    --muted-line: #9a9a9a;
  }
  * { box-sizing: border-box; margin: 0; padding: 0; }
  html, body {
    width: 1200px; height: 873px; overflow: hidden;
    background: var(--bg);
    font-family: "Lato", Arial, sans-serif;
  }
  .canvas { position: relative; width: 1200px; height: 873px; }

  .card {
    position: absolute;
    width: 560px; height: 320px;
    background: var(--card);
    border-radius: 18px;
    overflow: hidden;
  }
  .card__shapes { position: absolute; inset: 0; width: 100%; height: 100%; }

  /* Appointment side */
  .appointment { left: 40px; top: 90px; }
  .appointment__title {
    position: absolute; left: 34px; top: 40px;
    color: #fff; font-weight: 900; font-size: 26px; letter-spacing: 1px;
  }
  .appointment__divider {
    position: absolute; left: 34px; top: 80px; width: 380px; height: 1px;
    background: rgba(255,255,255,0.8);
  }
  .office-choice {
    position: absolute; top: 92px; display: flex; align-items: center; gap: 8px;
    color: #fff; font-size: 14px; font-weight: 700; text-transform: uppercase;
  }
  .office-choice__dot { width: 20px; height: 20px; border-radius: 50%; background: #fff; }
  .office-choice--ny { left: 34px; }
  .office-choice--bronx { left: 236px; }

  .field {
    position: absolute; left: 34px; display: flex; align-items: flex-end; gap: 14px;
    font-size: 16px; color: var(--ink);
  }
  .field__label { width: 44px; }
  .field__line { width: 430px; border-bottom: 1px solid var(--rule); height: 18px; }
  .field--for { top: 180px; }
  .field--date { top: 218px; }
  .field--time { top: 256px; }

  /* Contact side */
  .contact { left: 600px; top: 460px; }
  .brand {
    position: absolute; right: 34px; top: 50px; display: flex; align-items: center; gap: 12px;
  }
  .brand__mark { width: 22px; height: 22px; border-radius: 50%; background: var(--blue); }
  .brand__name {
    color: var(--blue); font-weight: 900; font-size: 24px; letter-spacing: 0.3px;
  }
  .tagline {
    position: absolute; right: 34px; top: 86px;
    color: var(--green); font-size: 15px;
  }
  .contact__rule {
    position: absolute; left: 30px; right: 30px; top: 122px; height: 1px; background: var(--muted-line);
  }
  .address {
    position: absolute; font-size: 15px; line-height: 1.3; color: var(--ink); font-style: normal;
  }
  .address--bronx { right: 34px; top: 134px; text-align: right; }
  .address--ny { left: 34px; top: 186px; }
  .phone {
    display: flex; align-items: center; gap: 6px; color: var(--blue); font-size: 15px; margin-top: 4px;
  }
  .address--bronx .phone { justify-content: flex-end; }
  .phone__icon { width: 18px; height: 18px; flex: none; }
</style>
</head>
<body>
<main class="canvas">

  <section class="card appointment" aria-label="Appointment card">
    <svg class="card__shapes" viewBox="0 0 560 320" preserveAspectRatio="none" aria-hidden="true">
      <polygon points="0,0 560,0 560,122 0,150" fill="var(--blue)"/>
      <polygon points="440,0 560,0 560,24 470,32" fill="var(--green)"/>
      <polygon points="0,150 560,122 560,134 0,162" fill="var(--blue-dark)" opacity="0.35"/>
      <polygon points="0,305 560,296 560,320 0,320" fill="var(--blue)"/>
      <polygon points="380,299 560,296 560,306 380,304" fill="var(--green)"/>
    </svg>
    <h2 class="appointment__title">APPOINTMENT</h2>
    <div class="appointment__divider"></div>
    <div class="office-choice office-choice--ny"><span class="office-choice__dot"></span>New York Office</div>
    <div class="office-choice office-choice--bronx"><span class="office-choice__dot"></span>Bronx Office</div>

    <div class="field field--for"><span class="field__label">For</span><span class="field__line"></span></div>
    <div class="field field--date"><span class="field__label">Date</span><span class="field__line"></span></div>
    <div class="field field--time"><span class="field__label">Time</span><span class="field__line"></span></div>
  </section>

  <section class="card contact" aria-label="Contact card">
    <svg class="card__shapes" viewBox="0 0 560 320" preserveAspectRatio="none" aria-hidden="true">
      <polygon points="0,292 230,282 250,320 0,320" fill="var(--blue)"/>
      <polygon points="230,282 560,262 560,280 250,300" fill="var(--green)"/>
    </svg>

    <div class="brand">
      <span class="brand__mark"></span>
      <span class="brand__name">DANIEL R. HOLLISTER MD PC</span>
    </div>
    <p class="tagline">Board Certified American Orthopedic Surgery</p>
    <div class="contact__rule"></div>

    <address class="address address--bronx">
      1487 Harrowgate Ave.<br>Suite KM7<br>Bronx, NY 10527
      <span class="phone">(718) 552 - 1948
        <svg class="phone__icon" viewBox="0 0 18 18" aria-label="Telephone"><circle cx="9" cy="9" r="9" fill="var(--green)"/><path d="M5 7.5c0-1.5 1.8-2.5 4-2.5s4 1 4 2.5l-1.6.4-.4-1.2H7l-.4 1.2z M6.5 8.5h5l1 4h-7z" fill="#fff"/></svg>
      </span>
      <span class="phone">(718) 552 - 7210
        <svg class="phone__icon" viewBox="0 0 18 18" aria-label="Fax"><circle cx="9" cy="9" r="9" fill="var(--green)"/><rect x="6" y="4.5" width="6" height="3.5" fill="#fff"/><rect x="4.5" y="8" width="9" height="5" rx="1" fill="#fff"/></svg>
      </span>
    </address>

    <address class="address address--ny">
      628 Fourth Ave.<br>Suite 42<br>New York, NY 10087
      <span class="phone">
        <svg class="phone__icon" viewBox="0 0 18 18" aria-label="Telephone"><circle cx="9" cy="9" r="9" fill="var(--green)"/><path d="M5 7.5c0-1.5 1.8-2.5 4-2.5s4 1 4 2.5l-1.6.4-.4-1.2H7l-.4 1.2z M6.5 8.5h5l1 4h-7z" fill="#fff"/></svg>
        (212) 734 - 2815
      </span>
    </address>
  </section>

</main>
</body>
</html>
```